Laundromat wall mural with logo, wash steps and soap dish instructions

Hi,
I am building a new laundromat and want to design a large wall mural containing a few different sections. The first piece would be a large image of my logo "Suds Harbor Laundromat" with my new tag line under it "A better Place to Wash". The next section would be general washing instructions: (step1) load clothes, (step 2) load soap, (step 3) select cycle (step 4) present payment (Quarters, Credit Card or Fennix/trove pay) (Step 5) Press start. Please use the wave from the logo to encase each of these 5 steps. Also please use an emblem in each wave to show each sections action. Such as they did in one of the example files I attached to this brief. The Final section would be the design for the soap compartment, describing where it goes. Please place the title "Where does the soap go?" above this section. The whole wall section will be 40 feet wide and 5 feet tall. I would like each section to flow aesthetically into the other. Feel free to use the logos waves and colors to bring everything together. I have attached examples of other store designs that I have found. The design will be above the washers that are placed against the wall.
I also placed a design of the mural that I wasn't completely impressed with so I opened the project to more designers.

Please let me know what other info you need.

Bests

Target Market(s)

laundromat customers

Industry/Entity Type

Laundromat

Font styles to use
Sans Serif

Colors
0054AA
0677BA
7BADD7
CADEEF
E8F1F8

Requirements
Must have
• The wave from my logo continuously flowing around the side and bottom borders.

```html
<!DOCTYPE html>
<html lang="en">
<head>
<meta charset="utf-8">
<title>Suds Harbor Laundromat – Wall Mural</title>
<link rel="stylesheet" href="https://fonts.googleapis.com/css2?family=Lilita+One&family=Montserrat:wght@500;700&display=swap">
<style>
  :root {
    --navy: #0b2f63;
    --deep: #0054AA;
    --mid: #0677BA;
    --sky: #7BADD7;
    --mist: #CADEEF;
    --foam: #E8F1F8;
    --white: #ffffff;
    --stage: #eef2f6;
  }
  html, body {
    margin: 0;
    padding: 0;
    width: 1200px;
    height: 358px;
    overflow: hidden;
    background: var(--stage);
  }
  .canvas {
    position: relative;
    width: 1200px;
    height: 358px;
    display: flex;
    align-items: center;
  }
  .mural { display: block; width: 1200px; height: 149px; }
  .display { font-family: "Lilita One", sans-serif; }
  .italic { font-style: italic; }
  .body-text { font-family: "Montserrat", sans-serif; }
</style>
</head>
<body>
<main class="canvas">
<svg class="mural" viewBox="0 0 2576 320" xmlns="http://www.w3.org/2000/svg" role="img" aria-label="Suds Harbor Laundromat wall mural: logo, five wash steps and soap compartment guide">
  <defs>
    <linearGradient id="stepsPanel" x1="0" y1="0" x2="1" y2="1">
      <stop offset="0" stop-color="#0a2550"/>
      <stop offset="0.45" stop-color="var(--deep)"/>
      <stop offset="1" stop-color="var(--mid)"/>
    </linearGradient>
    <linearGradient id="soapPanel" x1="0" y1="0" x2="0" y2="1">
      <stop offset="0" stop-color="var(--foam)"/>
      <stop offset="0.6" stop-color="var(--mist)"/>
      <stop offset="1" stop-color="var(--sky)"/>
    </linearGradient>
    <linearGradient id="taglineBand" x1="0" y1="0" x2="1" y2="0">
      <stop offset="0" stop-color="var(--mid)"/>
      <stop offset="1" stop-color="#1e8fd0"/>
    </linearGradient>
    <linearGradient id="dishPhoto" x1="0" y1="0" x2="0" y2="1">
      <stop offset="0" stop-color="#5d6066"/>
      <stop offset="1" stop-color="#9ea3a8"/>
    </linearGradient>
    <pattern id="waveLine" width="24" height="12" patternUnits="userSpaceOnUse">
      <path d="M0 6 Q6 0 12 6 T24 6" fill="none" stroke="var(--mist)" stroke-width="2"/>
    </pattern>
    <!-- border wave tiles -->
    <pattern id="waveBottomLight" x="0" y="296" width="48" height="24" patternUnits="userSpaceOnUse">
      <path d="M0 10 Q12 0 24 10 T48 10 V24 H0 Z" fill="var(--sky)"/>
    </pattern>
    <pattern id="waveBottom" x="24" y="302" width="48" height="18" patternUnits="userSpaceOnUse">
      <path d="M0 8 Q12 0 24 8 T48 8 V18 H0 Z" fill="var(--mid)"/>
    </pattern>
    <pattern id="waveLeft" x="0" y="0" width="20" height="48" patternUnits="userSpaceOnUse">
      <path d="M10 0 Q20 12 10 24 T10 48 H0 V0 Z" fill="var(--mid)"/>
    </pattern>
    <pattern id="waveRight" x="2556" y="0" width="20" height="48" patternUnits="userSpaceOnUse">
      <path d="M10 0 Q0 12 10 24 T10 48 H20 V0 Z" fill="var(--mid)"/>
    </pattern>
  </defs>

  <!-- logo field -->
  <rect class="logo-field" x="0" y="0" width="700" height="320" fill="var(--white)"/>
  <g class="logo">
    <circle cx="92" cy="125" r="16" fill="var(--mid)"/>
    <text class="display" x="120" y="148" font-size="62" fill="var(--mid)">SUDS HARBOR</text>
    <text class="display" x="122" y="200" font-size="40" fill="var(--mid)" letter-spacing="6">LAUNDROMAT</text>
  </g>

  <!-- tagline band -->
  <path class="tagline-band" d="M0 250 Q20 240 40 250 T80 250 T120 250 T160 250 T200 250 T240 250 T280 250 T320 250 T360 250 T400 250 T440 250 T480 250 T520 250 T560 250 T600 250 T640 250 L720 240 L720 320 L0 320 Z" fill="url(#taglineBand)"/>
  <text class="display italic" x="30" y="294" font-size="48" fill="var(--white)">A Better Place to Wash</text>

  <!-- steps panel -->
  <path class="steps-panel" d="M720 0 H1960 C2060 0 2060 320 1960 320 H760 C650 320 600 0 720 0 Z" fill="url(#stepsPanel)"/>
  <rect x="640" y="184" width="1395" height="12" fill="url(#waveLine)"/>

  <g class="step-emblems" fill="var(--mist)" stroke="#0a2550" stroke-width="5">
    <circle cx="818" cy="102" r="52"/>
    <circle cx="1073" cy="102" r="52"/>
    <circle cx="1318" cy="102" r="52"/>
    <circle cx="1582" cy="102" r="52"/>
    <circle cx="1837" cy="102" r="52"/>
  </g>

  <g class="step-icons" fill="none" stroke="var(--deep)" stroke-width="4" stroke-linecap="round" stroke-linejoin="round">
    <rect x="795" y="76" width="46" height="54" rx="4"/>
    <line x1="795" y1="88" x2="841" y2="88"/>
    <circle cx="818" cy="110" r="13"/>
    <rect x="1048" y="76" width="44" height="54" rx="4"/>
    <line x1="1048" y1="88" x2="1092" y2="88"/>
    <circle cx="1068" cy="110" r="12"/>
    <circle cx="1100" cy="104" r="4"/><circle cx="1104" cy="118" r="5"/>
    <path d="M1296 96 A24 24 0 0 1 1338 88"/>
    <path d="M1338 76 L1339 89 L1326 90"/>
    <path d="M1340 110 A24 24 0 0 1 1298 118"/>
    <path d="M1298 130 L1297 117 L1310 116"/>
    <rect x="1562" y="74" width="30" height="56" rx="5"/>
    <rect x="1580" y="94" width="30" height="20" rx="3" fill="var(--mist)"/>
    <text x="1584" y="109" font-size="10" font-family="Montserrat, sans-serif" fill="var(--deep)" stroke="none" font-weight="700">PAY</text>
    <path d="M1826 86 A20 20 0 1 0 1850 86"/>
    <line x1="1838" y1="76" x2="1838" y2="100"/>
  </g>

  <g class="step-numbers body-text" font-size="18" font-weight="700" text-anchor="middle" fill="var(--navy)">
    <circle cx="818" cy="190" r="15" fill="var(--white)" stroke="var(--deep)" stroke-width="3"/><text x="818" y="196">01</text>
    <circle cx="1073" cy="190" r="15" fill="var(--white)" stroke="var(--deep)" stroke-width="3"/><text x="1073" y="196">02</text>
    <circle cx="1318" cy="190" r="15" fill="var(--white)" stroke="var(--deep)" stroke-width="3"/><text x="1318" y="196">03</text>
    <circle cx="1582" cy="190" r="15" fill="var(--white)" stroke="var(--deep)" stroke-width="3"/><text x="1582" y="196">04</text>
    <circle cx="1837" cy="190" r="15" fill="var(--white)" stroke="var(--deep)" stroke-width="3"/><text x="1837" y="196">05</text>
  </g>

  <g class="step-labels display italic" font-size="34" fill="var(--white)" text-anchor="middle">
    <text x="818" y="252">Load Clothes</text>
    <text x="1073" y="252">Load Soap</text>
    <text x="1318" y="252">Select Cycle</text>
    <text x="1582" y="252">Present Payment</text>
    <text x="1837" y="252">Press Start</text>
  </g>
  <g class="step-note body-text" font-size="20" font-weight="500" fill="var(--white)" text-anchor="middle">
    <text x="1582" y="277">(Quarters, Credit Card</text>
    <text x="1582" y="299">or Fennix/trove pay)</text>
  </g>

  <!-- soap guide -->
  <path class="soap-panel" d="M2040 0 H2576 V320 H2040 C2080 240 2080 80 2040 0 Z" fill="url(#soapPanel)"/>
  <text class="display italic" x="2310" y="38" font-size="36" fill="var(--navy)" text-anchor="middle">Where does the soap go?</text>
  <rect x="2240" y="56" width="130" height="210" rx="8" fill="url(#dishPhoto)" role="img" aria-label="Photo of the washer soap compartment tray"/>

  <g class="dispenser-icons" fill="var(--white)" stroke="var(--deep)" stroke-width="4">
    <circle cx="2207" cy="175" r="19"/>
    <circle cx="2207" cy="223" r="19"/>
    <circle cx="2412" cy="175" r="19"/>
    <circle cx="2412" cy="223" r="19"/>
  </g>
  <g class="dispenser-arrows" fill="none" stroke="var(--mid)" stroke-width="7" stroke-linecap="round">
    <path d="M2228 165 Q2265 140 2290 180"/>
    <path d="M2228 225 Q2260 200 2288 232"/>
    <path d="M2391 165 Q2360 140 2335 180"/>
    <path d="M2391 225 Q2365 200 2337 232"/>
  </g>
  <g class="dispenser-labels body-text" font-size="12" font-weight="700" font-style="italic" fill="var(--navy)">
    <text x="2180" y="178" text-anchor="end">Fabric Softener</text>
    <text x="2180" y="227" text-anchor="end">Detergent</text>
    <text x="2438" y="171">Liquid only</text>
    <text x="2438" y="185">Detergent / Bleach</text>
    <text x="2438" y="227">Detergent</text>
  </g>

  <path class="pods-band" d="M2040 276 Q2060 268 2080 276 T2120 276 T2160 276 T2200 276 T2240 276 T2280 276 T2320 276 T2360 276 T2400 276 T2440 276 T2480 276 T2520 276 T2576 276 V320 H2030 Z" fill="var(--deep)"/>
  <text class="display italic" x="2290" y="302" font-size="30" fill="var(--white)" text-anchor="middle">Please place pods inside the washer</text>

  <!-- continuous logo wave along sides and bottom -->
  <g class="wave-border">
    <rect x="0" y="296" width="2576" height="24" fill="url(#waveBottomLight)"/>
    <rect x="0" y="302" width="2576" height="18" fill="url(#waveBottom)"/>
    <rect x="0" y="0" width="20" height="320" fill="url(#waveLeft)"/>
    <rect x="2556" y="0" width="20" height="320" fill="url(#waveRight)"/>
  </g>
</svg>
</main>
</body>
</html>
```